Anzeigengestaltung für einen einen ambulanten Pflegedienst
Zielgruppe
Insgesamt möchte ich gern drei Anzeigen für das Internet gestalten haben. Ich betreibe einen ambulanten Pflegedienst. Die erste Anzeige soll dazu dienen Kunden anzusprechen, die einen Unterstützungsbedarf und / oder einen Beratungsbedarf haben. Die zweite Anzeige soll dazu dienen neues Personal anzuwerben. Die dritte Anzeige soll speziell potenzielle Azubis ansprechen. Die Anzeigen sind gedacht für Chatterwall und Pixelora hauptsächlich. In den Druck sollte es schon 10cm x 8cm sein. Es wäre super wenn vielleicht auch eine Art Aufruf an ehrenamtliche Mitarbeiter erfolgt.
Aufgabenstellung
Die Anzeigen sollen den Stil der Homepage beibehalten. Freundlich, frisch und agil wirken. Alle sollten emotional ansprechend sein und gerade der für zukünftige Mitarbeiter sollte deutlich ein gutes Betriebsklima vermitteln. Als Datei habe ich einige Bilder, die bereits für die Homepage oder Flyer verwendet wurden hochgeladen. des Weiteren habe ich die einzelnen Seiten des Flyers hochgeladen.

```html
<!DOCTYPE html>
<html lang="de">
<head>
<meta charset="utf-8">
<title>Lindenhof Pflege – Wir sind für Sie da!</title>
<link href="https://fonts.googleapis.com/css2?family=Playfair+Display:wght@400&family=Quicksand:wght@500;700&display=swap" rel="stylesheet">
<style>
  :root {
    --teal: #4aafab;
    --green: #7cb13a;
    --text: #5f5f61;
    --band: #e1f0f9;
    --white: #ffffff;
    --ring: #eef0ea;
  }
  * { margin: 0; padding: 0; box-sizing: border-box; }
  html, body { width: 1200px; height: 960px; overflow: hidden; background: var(--white); }
  .ad {
    position: relative; width: 1200px; height: 960px; overflow: hidden;
    background: var(--white); color: var(--text);
    font-family: 'Quicksand', sans-serif; font-weight: 500;
  }
  .photo-shape, .accent-arcs { position: absolute; left: 0; top: 0; }
  .tagline {
    position: absolute; left: 60px; top: 62px;
    font-family: 'Playfair Display', serif; font-size: 33.5px; line-height: 1; color: var(--text);
  }
  .headline {
    position: absolute; left: 58px; top: 120px;
    font-weight: 700; font-size: 63px; line-height: 77px; color: var(--teal);
  }
  .headline-rule {
    position: absolute; left: 60px; top: 288px; width: 303px; height: 6px; background: var(--green);
  }
  .intro-line {
    position: absolute; font-size: 34px; line-height: 1; white-space: nowrap; color: var(--text);
  }
  .pill-outline {
    position: absolute; border: 3.5px solid var(--teal); border-radius: 40px;
  }
  .brand-badge {
    position: absolute; left: 958px; top: 412px; width: 212px; height: 212px;
    border-radius: 50%; background: var(--white); border: 4px solid var(--ring);
    display: flex; flex-direction: column; align-items: center; justify-content: center;
    gap: 20px; padding-top: 14px;
  }
  .brand-dot { width: 34px; height: 34px; border-radius: 50%; background: var(--teal); }
  .brand-name {
    font-weight: 700; font-size: 16px; letter-spacing: 0.3px; color: var(--text); text-align: center;
  }
  .services { position: absolute; list-style: none; font-size: 34px; line-height: 1; }
  .services li { position: absolute; white-space: nowrap; padding-left: 28px; }
  .services li::before {
    content: "+"; position: absolute; left: 0; top: 0; color: var(--green); font-weight: 500;
  }
  .services li.continued::before { content: none; }
  .services-left { left: 60px; top: 0; }
  .services-right { left: 523px; top: 0; }
  .contact-band {
    position: absolute; left: 0; top: 811px; width: 1200px; height: 149px; background: var(--band);
  }
  .cta-pill {
    position: absolute; top: 854px; height: 62px; border-radius: 31px;
    display: flex; align-items: center; justify-content: center;
    font-family: 'Playfair Display', serif; color: var(--white); white-space: nowrap;
  }
  .cta-question { left: 35px; width: 409px; background: var(--green); font-size: 34px; }
  .cta-contact { left: 476px; width: 686px; background: var(--teal); font-size: 32px; }
</style>
</head>
<body>
<main class="ad">
  <svg class="photo-shape" width="1200" height="960" viewBox="0 0 1200 960" role="img" aria-label="Foto: eine Pflegekraft legt ihre Hand auf die Hand einer älteren Person am Griff eines Rollators">
    <defs>
      <clipPath id="photoClip"><circle cx="1147" cy="-33" r="592"/></clipPath>
      <linearGradient id="photoBase" x1="0" y1="0" x2="1" y2="1">
        <stop offset="0" stop-color="#e4e8ec"/>
        <stop offset="0.55" stop-color="#dfe3e7"/>
        <stop offset="1" stop-color="#e9edf0"/>
      </linearGradient>
      <radialGradient id="skinWarm" cx="0.5" cy="0.5" r="0.5">
        <stop offset="0" stop-color="#d49a82"/>
        <stop offset="0.55" stop-color="#dcae98" stop-opacity="0.85"/>
        <stop offset="1" stop-color="#e2c6b8" stop-opacity="0"/>
      </radialGradient>
      <radialGradient id="skinLight" cx="0.5" cy="0.5" r="0.5">
        <stop offset="0" stop-color="#e8b9a4"/>
        <stop offset="1" stop-color="#ebcdbf" stop-opacity="0"/>
      </radialGradient>
      <radialGradient id="greyTone" cx="0.5" cy="0.5" r="0.5">
        <stop offset="0" stop-color="#8d9094"/>
        <stop offset="1" stop-color="#b8bcc0" stop-opacity="0"/>
      </radialGradient>
      <radialGradient id="softWhite" cx="0.5" cy="0.5" r="0.5">
        <stop offset="0" stop-color="#fbfbf9"/>
        <stop offset="1" stop-color="#f4f5f4" stop-opacity="0"/>
      </radialGradient>
      <radialGradient id="mintTone" cx="0.5" cy="0.5" r="0.5">
        <stop offset="0" stop-color="#cfe8e6"/>
        <stop offset="1" stop-color="#dfeceb" stop-opacity="0"/>
      </radialGradient>
    </defs>
    <g clip-path="url(#photoClip)">
      <rect x="540" y="0" width="660" height="560" fill="url(#photoBase)"/>
      <ellipse cx="1170" cy="40" rx="90" ry="120" fill="url(#mintTone)"/>
      <ellipse cx="880" cy="330" rx="330" ry="70" fill="url(#greyTone)" transform="rotate(8 880 330)"/>
      <ellipse cx="930" cy="230" rx="250" ry="130" fill="url(#skinWarm)" transform="rotate(12 930 230)"/>
      <ellipse cx="880" cy="190" rx="170" ry="80" fill="url(#skinLight)" transform="rotate(-10 880 190)"/>
      <ellipse cx="1150" cy="190" rx="110" ry="190" fill="url(#softWhite)" transform="rotate(-20 1150 190)"/>
    </g>
  </svg>

  <svg class="accent-arcs" width="1200" height="960" viewBox="0 0 1200 960" aria-hidden="true">
    <path d="M487 149 C484 78 534 61 573 62 S629 67 643 74" fill="none" stroke="var(--teal)" stroke-width="7" stroke-linecap="round"/>
    <path d="M515 209 C520 145 529 117 545 109 S629 100 662 116" fill="none" stroke="var(--green)" stroke-width="7" stroke-linecap="round"/>
  </svg>

  <p class="tagline">Pflege mit Herz &amp; Seele</p>
  <h1 class="headline">Wir sind<br>für Sie da!</h1>
  <div class="headline-rule"></div>

  <div class="pill-outline" style="left:309px; top:373px; width:341px; height:64px;"></div>
  <div class="pill-outline" style="left:36px; top:426px; width:222px; height:64px;"></div>
  <p class="intro-line" style="left:60px; top:333px;">Für unseren ambulanten Pflege-</p>
  <p class="intro-line" style="left:60px; top:387px;">dienst steht die</p>
  <p class="intro-line" style="left:330px; top:387px;">Pflege von Mensch</p>
  <p class="intro-line" style="left:70px; top:443px;">zu Mensch</p>
  <p class="intro-line" style="left:272px; top:443px;">im Mittelpunkt.</p>

  <div class="brand-badge">
    <span class="brand-dot"></span>
    <span class="brand-name">LINDENHOF PFLEGE</span>
  </div>

  <ul class="services services-left">
    <li style="top:564px;">Grundpflege</li>
    <li style="top:623px;">Behandlungspflege</li>
    <li style="top:682px;">Beratungseinsatz</li>
    <li style="top:741px;">Verhinderungspflege</li>
  </ul>
  <ul class="services services-right">
    <li style="top:564px;">Entlastungs- und</li>
    <li class="continued" style="top:610px;">Betreuungsangebote</li>
    <li style="top:669px;">Hauswirtschaftliche Leistungen</li>
    <li style="top:729px;">Sofortige Hilfen</li>
  </ul>

  <div class="contact-band"></div>
  <div class="cta-pill cta-question">Wie können wir helfen?</div>
  <div class="cta-pill cta-contact">www.lindenhof-pflege.de / 03491-55 72 40</div>
</main>
</body>
</html>
```